Corbel Crest Lighting - Commercial & Residential Landscape Lighting

Landscape Lighting Services & Design: Create a website for our landscape lighting company. We would like the design to be tailored around this description:
Illuminate with Confidence. Designed with Precision. Installed with Care.
Locally and veteran-owned, we take pride in transforming outdoor spaces through innovative lighting solutions tailored to your vision. From landscape and holiday lighting to permanent installations, our effortless process and expert design deliver breathtaking results and lasting curb appeal. Backed by a lifetime warranty and quarterly service options, our commitment to quality and customer satisfaction is unwavering. Try before you buy and experience your home in a whole new light with our complimentary demo kit — see the stunning effects before you decide.
- Also, add in this information as well; Outdoor Lighting not only beautifies spaces but also significantly enhances safety by illuminating your home or business. Beautifully lit entrances deter potential intruders, making your home a safer place for your loved ones. we also offer quarterly service plans to ensure lighting equipment continues to operate & illuminate effectively throughout the year. Also mention we provide free estimates and we are offering a 10% discount to military, veterans, and first responders.

Target Market(s)

Luxury market

Industry/Entity Type

Landscape Lighting - Residential & Commercial Lighting Services

Coding

Coded - Design and coding required

Number of Pages Required

2 page

Colors
00AB8E
00BBA5
67D7C9
C6EFE9
E9F9F6
59FF00
82FF00
B8FF75
E3FFCB
F4FFEA
FFC000
F8CF3A
FAE287
FDF2CF
FEFAEE

Requirements
Must have
• a lead generation button where people can submit their information for us to reach out to them and schedule their free estimate, homepage, about page, contact page, products and services page, user friendly, easy to navigate, and it also must be engaging and eye popping, as well as appealing to the luxury market. Please use colors; verdent green, dark green, ivory, and sunny yellow. Also, include an about page that references our story; Glen is retired Army and he opened a fitness studio in 2017 with his wife Rosalind. He has installed low voltage lighting in every home he lived in and for his friends and family over the years and decided to open his own business because he is passionate about beautifying outdoor landscapes and highlighting a properties full potential, not only in the day but at night as well all while providing safety and security for his clients. Having a deep respect for nature and landscaping, he wants to provide the same care and quality to each of his clients as he has in the fitness industry for decades. He believes small businesses are the back bone of America and he's excited to provide a service that is all to often neglected in the design of a home.
Nice to have
• I would like to have a clear intent and purpose, engaging web design, clear call to action, optimized for search engines, mobile friendy design, security measures, credibility indicators

```html
<!DOCTYPE html>
<html lang="en">
<head>
<meta charset="utf-8">
<title>Corbel Crest Lighting – Commercial &amp; Residential Landscape Lighting</title>
<link href="https://fonts.googleapis.com/css2?family=Jost:wght@300;400;500&family=Montserrat:wght@400;500;600;700&display=swap" rel="stylesheet">
<style>
:root{
  --teal:#00AB8E;
  --teal-2:#00BBA5;
  --teal-3:#67D7C9;
  --mint:#E9F9F6;
  --mint-2:#C6EFE9;
  --yellow:#FFC000;
  --yellow-2:#F8CF3A;
  --ivory:#FEFAEE;
  --ink:#1d1d1d;
  --text:#444;
  --white:#fff;
  --glow:rgba(255,196,110,.75);
  --glow-soft:rgba(255,190,100,.35);
}
*{box-sizing:border-box;margin:0;padding:0}
html,body{width:1200px;height:4351px;overflow:hidden}
body{position:relative;background:var(--white);font-family:"Montserrat",sans-serif;color:var(--text)}
.abs{position:absolute}
.heading{font-family:"Jost",sans-serif;font-weight:400;color:var(--ink);text-transform:uppercase;letter-spacing:-.5px}
.rule{display:inline-block;height:3px;background:var(--yellow);vertical-align:middle}
.btn{display:inline-flex;align-items:center;justify-content:center;font-size:11px;font-weight:500;color:#fff;background:var(--teal);text-decoration:none}

/* nav */
.nav{top:0;left:0;width:1200px;height:54px;background:#fff}
.brand{left:120px;top:10px;font-weight:600;font-size:17px;color:#c0213a;line-height:34px;letter-spacing:.5px}
.menu{right:122px;top:0;height:54px;display:flex;align-items:center;gap:30px;font-size:11.5px;color:#333}
.menu .active{color:var(--teal)}
.menu .btn{height:30px;padding:0 12px;font-size:11.5px;margin-left:-4px}

/* photo fills */
.hero{top:54px;left:0;width:1200px;height:640px;
  background:
    radial-gradient(ellipse 260px 200px at 820px 560px,rgba(215,190,150,.55),transparent 70%),
    radial-gradient(ellipse 120px 80px at 900px 330px,var(--glow-soft),transparent 70%),
    radial-gradient(ellipse 90px 70px at 1040px 260px,var(--glow-soft),transparent 70%),
    radial-gradient(ellipse 500px 300px at 1000px 120px,rgba(110,130,90,.45),transparent 70%),
    linear-gradient(180deg,#1b231d 0%,#27321f 40%,#3e4a2c 70%,#5f6246 100%)}
.hero::after{content:"";position:absolute;inset:0;background:linear-gradient(90deg,rgba(10,14,10,.55),rgba(10,14,10,0) 60%)}
.about-photo{left:135px;top:760px;width:445px;height:372px;border-radius:12px;
  background:
    radial-gradient(ellipse 70px 50px at 230px 210px,var(--glow),transparent 70%),
    radial-gradient(ellipse 160px 70px at 220px 220px,rgba(200,110,70,.55),transparent 75%),
    radial-gradient(ellipse 60px 30px at 130px 255px,var(--glow-soft),transparent 70%),
    radial-gradient(ellipse 60px 30px at 300px 255px,var(--glow-soft),transparent 70%),
    linear-gradient(180deg,#4a5a6a 0%,#2a3532 30%,#2b3a24 60%,#3f5a2a 100%)}
.pic-res{background:
    radial-gradient(ellipse 30px 55px at 110px 100px,var(--glow),transparent 70%),
    radial-gradient(ellipse 30px 55px at 220px 95px,var(--glow),transparent 70%),
    radial-gradient(ellipse 30px 55px at 340px 110px,var(--glow),transparent 70%),
    radial-gradient(ellipse 300px 90px at 200px 220px,rgba(120,200,60,.55),transparent 75%),
    linear-gradient(180deg,#151a14,#1f2a16 55%,#3c6a1c 100%)}
.pic-com{background:
    radial-gradient(ellipse 90px 80px at 260px 140px,rgba(255,200,120,.85),transparent 70%),
    radial-gradient(ellipse 200px 140px at 250px 150px,rgba(180,120,50,.4),transparent 75%),
    linear-gradient(150deg,#2c3d14,#4d6a22 45%,#1e2a10)}
.pic-path{background:
    radial-gradient(ellipse 120px 40px at 140px 80px,rgba(90,200,90,.6),transparent 75%),
    radial-gradient(ellipse 40px 30px at 230px 40px,var(--glow-soft),transparent 70%),
    linear-gradient(180deg,#1d2a3a,#22402c 55%,#3a4a58 100%)}
.pic-event{background:
    radial-gradient(ellipse 260px 14px at 150px 22px,rgba(255,220,150,.55),transparent 75%),
    radial-gradient(ellipse 80px 40px at 150px 90px,rgba(220,170,110,.45),transparent 75%),
    linear-gradient(180deg,#141a16,#24301e 60%,#34462a)}
.pic-arch{background:
    linear-gradient(180deg,transparent 70%,rgba(230,230,230,.55) 80%,transparent 95%),
    linear-gradient(90deg,#7a4a1e,#c8955a 30%,#b07a40 55%,#8aa86a 78%,#4e7a38)}
.proj-side-l{background:
    radial-gradient(ellipse 50px 90px at 20px 300px,rgba(255,170,70,.8),transparent 70%),
    linear-gradient(160deg,#6f6a5a,#3a4430 50%,#26301f)}
.proj-main{background:
    radial-gradient(ellipse 150px 180px at 230px 140px,rgba(250,225,180,.8),transparent 70%),
    radial-gradient(ellipse 260px 120px at 230px 300px,rgba(210,140,80,.55),transparent 75%),
    radial-gradient(ellipse 90px 60px at 560px 330px,rgba(200,120,80,.45),transparent 70%),
    radial-gradient(ellipse 160px 200px at 620px 500px,rgba(200,210,200,.25),transparent 70%),
    linear-gradient(180deg,#4a6a8a 0%,#355070 25%,#2a3a30 55%,#1c2a1a 100%)}
.proj-side-r{background:
    radial-gradient(ellipse 50px 60px at 90px 180px,rgba(40,40,40,.6),transparent 70%),
    linear-gradient(180deg,#a8b880,#7f9a52 50%,#5a7a34)}
.pic-contact{background:
    radial-gradient(ellipse 40px 40px at 95px 190px,rgba(255,230,170,.95),transparent 70%),
    radial-gradient(ellipse 140px 100px at 110px 220px,var(--glow-soft),transparent 75%),
    radial-gradient(ellipse 220px 90px at 260px 300px,rgba(140,190,60,.5),transparent 75%),
    linear-gradient(180deg,#1e2818,#34461f 50%,#4a6a24 100%)}

/* hero */
.hero-title{left:120px;top:236px;font-size:47px;line-height:64px;color:#fff}
.hero-sub{left:121px;top:366px;font-size:13.5px;color:#fff}
.hero-btns{left:121px;top:411px;display:flex;gap:14px}
.hero-btns .btn{height:35px;width:114px;font-size:11.5px}
.hero-btns .ghost{background:transparent;border:1.5px solid #fff;width:164px}
.hero-curve{left:0;top:500px;width:1200px;height:200px}

/* about */
.about-frame{left:122px;top:749px;width:470px;height:396px;border:2px solid var(--yellow);border-radius:14px}
.about-title{left:671px;top:775px;font-size:40px}
.about-text{left:671px;top:830px;width:405px;font-size:11px;line-height:17.6px;color:#333}
.about-btn{left:673px;top:1050px;width:139px;height:36px}
.about-deco{left:1110px;top:680px;font-size:100px;color:#eccfd3;writing-mode:vertical-rl;letter-spacing:6px;line-height:1}

/* categories */
.cat-band{left:0;top:1208px;width:1200px;height:516px;background:var(--mint)}
.cat{top:1271px;height:389px;background:#fff;border:2px solid var(--teal-3);border-radius:8px}
.cat .pic{position:absolute;left:12px;top:12px;right:12px;height:246px;border-radius:4px}
.cat h3{position:absolute;left:16px;top:272px;font-weight:500;font-size:22px;color:#222}
.cat p{position:absolute;left:16px;top:311px;width:310px;font-size:11.5px;line-height:15px;color:#333}
.cat .go{position:absolute;right:18px;bottom:16px;width:40px;height:40px;border-radius:50%;background:var(--yellow)}
.cat-badge{left:514px;top:1440px;width:168px;height:90px;background:#fff;display:flex;align-items:center;justify-content:center;font-weight:600;font-size:16px;color:#c0213a;text-align:center;line-height:20px}

/* services */
.svc-title{left:122px;top:1772px;font-size:40px}
.svc-all{left:938px;top:1779px;width:139px;height:36px}
.svc{top:1851px;width:306px;height:256px;border:2px solid var(--teal-3);border-radius:8px;background:#fff;text-align:center}
.svc .pic{position:absolute;left:8px;top:8px;right:8px;height:124px}
.svc .ico{position:absolute;left:50%;top:108px;margin-left:-27px;width:54px;height:54px;border-radius:50%;background:#fff;border:2px solid var(--teal-3)}
.svc h3{position:absolute;left:0;right:0;top:170px;font-weight:600;font-size:17.5px;color:#222}
.svc p{position:absolute;left:36px;right:36px;top:199px;font-size:11px;line-height:13.5px;color:#444}

/* why */
.why-band{left:0;top:2168px;width:1200px;height:330px;background:var(--mint)}
.why-title{left:0;width:1200px;top:2220px;text-align:center;font-size:40px}
.why{top:2319px;height:118px;background:#fff;border:2px solid var(--teal-3);border-radius:6px;text-align:center}
.why .ico{position:absolute;left:50%;top:-22px;margin-left:-33px;width:66px;height:66px;border-radius:50%;background:#fff;border:2px solid var(--teal-3)}
.why span{position:absolute;left:0;right:0;top:60px;font-size:15px;line-height:17px;font-weight:500;color:#333}
.why.on{background:var(--teal);border-color:var(--teal)}
.why.on span{color:#fff}
.why.on .ico{border-color:var(--teal)}
.arrow-c{width:34px;height:34px;border-radius:50%;border:1.5px solid var(--teal-3);background:#fff}

/* projects */
.proj-title{left:0;width:1200px;top:2550px;text-align:center;font-size:40px}
.proj-main{left:184px;top:2653px;width:832px;height:546px}
.proj-side-l{left:0;top:2653px;width:160px;height:546px}
.proj-side-r{left:1039px;top:2653px;width:161px;height:546px}

/* testimonials */
.test-title{left:0;width:1200px;top:3250px;text-align:center;font-size:40px}
.quote{top:3363px;height:195px;background:var(--mint);border-bottom:3px solid var(--teal);border-radius:4px}
.quote .av{position:absolute;left:50px;top:20px;width:84px;height:84px;border-radius:50%;background:linear-gradient(160deg,#d6dde0,#7d8c90)}
.quote .name{position:absolute;left:157px;top:48px;font-weight:600;font-size:12.5px;color:#222}
.quote .role{position:absolute;left:157px;top:69px;font-size:10px;color:#333}
.quote .stars{position:absolute;left:156px;top:84px}
.quote blockquote{position:absolute;left:50px;right:30px;top:142px;font-size:11px;line-height:18px;color:#333}
.quote .mark{position:absolute;right:48px;top:-24px;width:48px;height:48px;border-radius:50%;background:var(--yellow);color:#fff;font-family:Georgia,serif;font-size:44px;font-weight:700;line-height:62px;text-align:center}

/* contact */
.footer-bg{left:0;top:3950px;width:1200px;height:401px}
.contact{left:122px;top:3622px;width:956px;height:426px;background:var(--yellow);border-radius:10px;overflow:hidden}
.contact .pic{position:absolute;left:0;top:0;width:480px;height:426px;clip-path:ellipse(100% 118% at 0% 50%)}
.contact h2{position:absolute;left:598px;top:50px;font-size:40px}
.field{position:absolute;background:#fff;font-size:9.5px;color:#777;padding:10px 10px}
.submit{position:absolute;left:656px;top:344px;width:106px;height:34px;background:var(--teal);display:flex;align-items:center;color:#fff;font-size:11.5px;font-weight:500}
.submit b{display:block;width:60px;text-align:center;font-weight:500}
.submit i{display:flex;align-items:center;justify-content:center;width:40px;height:28px;background:#fff;margin-left:2px}

/* footer */
.f-brand{left:122px;top:4118px;font-size:40px;font-weight:400;color:#fff;line-height:50px}
.f-tag{left:122px;top:4170px;font-size:8px;letter-spacing:2px;color:#fff;text-transform:uppercase}
.f-social{left:122px;top:4207px;display:flex;gap:11px}
.f-social span{width:26px;height:26px;border-radius:50%;border:1.5px solid var(--yellow)}
.f-col h4{font-size:13px;font-weight:500;color:#fff;text-transform:uppercase;margin-bottom:14px}
.f-col a,.f-col p{display:block;font-size:10.5px;color:#fff;text-decoration:none;margin-bottom:13px}
.f-col .em{color:var(--yellow)}
.news{left:852px;top:4176px;width:225px;height:34px;display:flex}
.news span{flex:1;border:1px solid var(--yellow);font-size:9.5px;color:#fff;padding:11px 12px}
.news b{width:73px;background:var(--yellow);font-size:10.5px;font-weight:600;color:#222;display:flex;align-items:center;justify-content:center}
.f-line{left:122px;top:4284px;width:955px;height:1px;background:rgba(255,255,255,.55)}
.f-copy{left:122px;top:4293px;font-size:9.5px;color:#fff}
.f-legal{right:123px;top:4293px;font-size:9.5px;color:#fff}
</style>
</head>
<body>

<header class="nav abs">
  <div class="brand abs">Corbel Crest Lighting</div>
  <nav class="menu abs">
    <span class="active">Home</span><span>About Us</span><span>Products</span><span>Services</span><span>Contact Us</span>
    <a class="btn" href="#contact">Get a Free Quote</a>
  </nav>
</header>

<section class="hero abs" role="img" aria-label="Evening photo of a lit stone garden path winding between trees and shrubs"></section>
<h1 class="hero-title heading abs">Illuminate your outdoors <span class="rule" style="width:98px;margin-left:8px"></span><br>with expert lighting design</h1>
<p class="hero-sub abs">Professional Commercial &amp; Residential Landscape Lighting Solutions</p>
<div class="hero-btns abs"><a class="btn" href="#">View Gallery</a><a class="btn ghost" href="#">Schedule Consultation</a></div>
<svg class="hero-curve abs" viewBox="0 0 1200 200" preserveAspectRatio="none" aria-hidden="true">
  <path d="M0 60 C260 200 640 210 1200 40 L1200 200 L0 200 Z" fill="#fff"/>
  <path d="M0 60 C260 200 640 210 1200 40" fill="none" stroke="var(--yellow)" stroke-width="9"/>
</svg>

<div class="about-deco abs">CORBEL</div>
<div class="about-frame abs"></div>
<div class="about-photo abs" role="img" aria-label="Brick house at dusk with landscape lighting on the lawn and shrubs"></div>
<h2 class="about-title heading abs">About us <span class="rule" style="width:92px;margin-left:4px"></span></h2>
<p class="about-text abs">Glen is retired Army and he opened a fitness studio in 2017 with his wife Rosalind. He has installed low voltage lighting in every home he lived in and for his friends and family over the years and decided to open his own business because he is passionate about beautifying outdoor landscapes and highlighting a properties full potential, not only in the day but at night as well all while providing safety and security for his clients. Having a deep respect for nature and landscaping, he wants to provide the same care and quality to each of his clients as he has in the fitness industry for decades. He believes small businesses are the back bone of America and he's excited to provide a service that is all to often neglected in the design of a home.</p>
<a class="about-btn btn abs" href="#">View Gallery</a>

<div class="cat-band abs"></div>
<article class="cat abs" style="left:128px;width:460px">
  <div class="pic pic-res" role="img" aria-label="Night lawn with hanging lanterns under a large tree"></div>
  <h3>Residential Landscape Lighting</h3>
  <p>Transform your home's exterior into a welcoming, elegant retreat with custom lighting for gardens, walkways, patios, and more.</p>
  <svg class="go" viewBox="0 0 40 40" aria-hidden="true"><path d="M17 13l7 7-7 7" fill="none" stroke="#fff" stroke-width="2.5"/></svg>
</article>
<article class="cat abs" style="left:608px;width:469px">
  <div class="pic pic-com" role="img" aria-label="Lit garden lantern among tropical plants at night"></div>
  <h3>Commercial Outdoor Lighting</h3>
  <p>Attract customers and improve safety with lighting that enhances curb appeal and highlights architectural elements.</p>
  <svg class="go" viewBox="0 0 40 40" aria-hidden="true"><path d="M17 13l7 7-7 7" fill="none" stroke="#fff" stroke-width="2.5"/></svg>
</article>
<div class="cat-badge abs">Corbel Crest<br>Lighting</div>

<h2 class="svc-title heading abs">Our services <span class="rule" style="width:92px;margin-left:4px"></span></h2>
<a class="svc-all btn abs" href="#">View all Services</a>
<article class="svc abs" style="left:122px">
  <div class="pic pic-path" role="img" aria-label="Lit pathway through a city plaza at night"></div>
  <svg class="ico" viewBox="0 0 54 54" aria-hidden="true"><path d="M19 35l8-16 8 16M27 19v-4" fill="none" stroke="var(--teal)" stroke-width="1.8"/></svg>
  <h3>Path &amp; Walkway Lighting</h3>
  <p>Guide guests safely with functional and stylish pathway lighting.</p>
</article>
<article class="svc abs" style="left:446px">
  <div class="pic pic-event" role="img" aria-label="Outdoor dinner under string lights"></div>
  <svg class="ico" viewBox="0 0 54 54" aria-hidden="true"><path d="M15 20q12 8 24 0M19 23v6M27 25v6M35 23v6" fill="none" stroke="var(--teal)" stroke-width="1.8"/></svg>
  <h3>Holiday &amp; Event Lighting</h3>
  <p>From festive holiday setups to one-time events, we design and install custom lighting for any occasion.</p>
</article>
<article class="svc abs" style="left:771px">
  <div class="pic pic-arch" role="img" aria-label="Wood-clad terrace with lounge chairs and lit walls"></div>
  <svg class="ico" viewBox="0 0 54 54" aria-hidden="true"><rect x="16" y="20" width="22" height="14" fill="none" stroke="var(--teal)" stroke-width="1.8"/><path d="M16 27h22" stroke="var(--teal)" stroke-width="1.8"/></svg>
  <h3>Architectura Lighting</h3>
  <p>Showcase your property's best features with lighting designed to highlight textures, shapes, and details.</p>
</article>

<div class="why-band abs"></div>
<h2 class="why-title heading abs"><span class="rule" style="width:92px;margin-right:8px"></span>Why choose us<span class="rule" style="width:92px;margin-left:8px"></span></h2>
<svg class="arrow-c abs" style="left:62px;top:2361px" viewBox="0 0 34 34" aria-hidden="true"><path d="M19 11l-6 6 6 6" fill="none" stroke="var(--teal)" stroke-width="1.6"/></svg>
<svg class="arrow-c abs" style="left:1100px;top:2361px" viewBox="0 0 34 34" aria-hidden="true"><path d="M15 11l6 6-6 6" fill="none" stroke="var(--teal)" stroke-width="1.6"/></svg>
<div class="why abs" style="left:122px;width:180px"><svg class="ico" viewBox="0 0 66 66" aria-hidden="true"><circle cx="33" cy="25" r="5" fill="none" stroke="var(--teal)" stroke-width="1.6"/><path d="M22 44v-6h22v6M33 30v8" fill="none" stroke="var(--teal)" stroke-width="1.6"/></svg><span>Custom Lighting<br>Designs</span></div>
<div class="why on abs" style="left:316px;width:179px"><svg class="ico" viewBox="0 0 66 66" aria-hidden="true"><circle cx="33" cy="26" r="7" fill="none" stroke="var(--teal)" stroke-width="1.6"/><path d="M21 46q12-16 24 0" fill="none" stroke="var(--teal)" stroke-width="1.6"/></svg><span>Professional<br>Installation</span></div>
<div class="why abs" style="left:509px;width:181px"><svg class="ico" viewBox="0 0 66 66" aria-hidden="true"><circle cx="33" cy="29" r="9" fill="none" stroke="var(--teal)" stroke-width="1.6"/><path d="M29 42h8M30 46h6" stroke="var(--teal)" stroke-width="1.6"/></svg><span>Energy-Efficient<br>LED Systems</span></div>
<div class="why abs" style="left:703px;width:179px"><svg class="ico" viewBox="0 0 66 66" aria-hidden="true"><path d="M33 18l12 5v9c0 8-6 13-12 15-6-2-12-7-12-15v-9z" fill="none" stroke="var(--teal)" stroke-width="1.6"/><path d="M28 33l4 4 7-8" fill="none" stroke="var(--teal)" stroke-width="1.6"/></svg><span>Licensed &amp; Insured<br>Technicians</span></div>
<div class="why abs" style="left:896px;width:181px"><svg class="ico" viewBox="0 0 66 66" aria-hidden="true"><circle cx="33" cy="33" r="12" fill="none" stroke="var(--teal)" stroke-width="1.6"/><path d="M33 27v6l4 3" fill="none" stroke="var(--teal)" stroke-width="1.6"/></svg><span>Ongoing Support &amp;<br>Maintenance</span></div>

<h2 class="proj-title heading abs"><span class="rule" style="width:92px;margin-right:8px"></span>Featured projects<span class="rule" style="width:92px;margin-left:8px"></span></h2>
<div class="proj-side-l abs" role="img" aria-label="Close view of a warm filament bulb outdoors"></div>
<div class="proj-main abs" role="img" aria-label="Brick house with lit gable and walkway lights at dusk"></div>
<div class="proj-side-r abs" role="img" aria-label="Lantern post light on a wooden pillar in a garden"></div>
<svg class="abs" style="left:70px;top:2903px" width="30" height="50" viewBox="0 0 30 50" aria-hidden="true"><path d="M25 3L5 25l20 22" fill="none" stroke="#fff" stroke-width="2.5"/></svg>
<svg class="abs" style="left:1100px;top:2903px" width="30" height="50" viewBox="0 0 30 50" aria-hidden="true"><path d="M5 3l20 22L5 47" fill="none" stroke="#fff" stroke-width="2.5"/></svg>

<h2 class="test-title heading abs"><span class="rule" style="width:92px;margin-right:8px"></span>Customer testimonials<span class="rule" style="width:92px;margin-left:8px"></span></h2>
<svg class="arrow-c abs" style="left:62px;top:3442px" viewBox="0 0 34 34" aria-hidden="true"><path d="M19 11l-6 6 6 6" fill="none" stroke="var(--teal)" stroke-width="1.6"/></svg>
<svg class="arrow-c abs" style="left:1100px;top:3442px" viewBox="0 0 34 34" aria-hidden="true"><path d="M15 11l6 6-6 6" fill="none" stroke="var(--teal)" stroke-width="1.6"/></svg>
<article class="quote abs" style="left:122px;width:454px">
  <div class="av" role="img" aria-label="Portrait of the reviewer"></div>
  <div class="name">NORA P.</div><div class="role">Home owner</div>
  <svg class="stars" width="82" height="14" viewBox="0 0 82 14" aria-hidden="true"><g fill="var(--yellow)"><path id="st" d="M7 0l2 5h5l-4 3 1.6 5L7 10l-4.6 3L4 8 0 5h5z"/><use href="#st" x="17"/><use href="#st" x="34"/><use href="#st" x="51"/><use href="#st" x="68"/></g></svg>
  <blockquote>"The lighting completely changed the look of our backyard. It's like a resort now!"</blockquote>
  <div class="mark">”</div>
</article>
<article class="quote abs" style="left:624px;width:453px">
  <div class="av" role="img" aria-label="Portrait of the reviewer"></div>
  <div class="name">OWEN T.</div><div class="role">Business Owner</div>
  <svg class="stars" width="82" height="14" viewBox="0 0 82 14" aria-hidden="true"><g fill="var(--yellow)"><use href="#st"/><use href="#st" x="17"/><use href="#st" x="34"/><use href="#st" x="51"/><use href="#st" x="68"/></g></svg>
  <blockquote>"Professional, on time, and the results were fantastic. Our office exterior has never looked better."</blockquote>
  <div class="mark">”</div>
</article>

<svg class="footer-bg abs" viewBox="0 0 1200 401" preserveAspectRatio="none" aria-hidden="true">
  <path d="M0 0 C60 10 110 40 140 98 L1060 98 C1090 60 1140 30 1200 22 L1200 401 L0 401 Z" fill="var(--teal)"/>
  <path d="M0 0 C60 10 110 40 140 98" fill="none" stroke="var(--yellow)" stroke-width="7"/>
  <path d="M1060 98 C1090 60 1140 30 1200 22" fill="none" stroke="var(--yellow)" stroke-width="7"/>
</svg>

<section class="contact abs" id="contact">
  <div class="pic pic-contact" role="img" aria-label="Garden at dusk with a lit bollard light and lawn"></div>
  <h2 class="heading">Contact us</h2>
  <div class="field" style="left:510px;top:143px;width:196px;height:36px">First name</div>
  <div class="field" style="left:710px;top:143px;width:198px;height:36px">Last name</div>
  <div class="field" style="left:510px;top:186px;width:196px;height:36px">Email</div>
  <div class="field" style="left:710px;top:186px;width:198px;height:36px">Phone Number</div>
  <div class="field" style="left:510px;top:228px;width:398px;height:72px">Message</div>
  <div class="submit"><b>Submit</b><i><svg width="18" height="18" viewBox="0 0 18 18" aria-hidden="true"><path d="M2 8l14-6-6 14-2-6z" fill="none" stroke="var(--teal)" stroke-width="1.4"/></svg></i></div>
</section>

<div class="f-brand abs">CORBEL</div>
<div class="f-tag abs">Corbel Crest Lighting</div>
<div class="f-social abs"><span></span><span></span><span></span></div>
<div class="f-col abs" style="left:453px;top:4112px">
  <h4>Quick Links</h4><a href="#">Home</a><a href="#">About Us</a><a href="#">Products</a><a href="#">Services</a>
</div>
<div class="f-col abs" style="left:615px;top:4112px">
  <h4>Contact Info</h4><p class="em">✉ hello@corbelcrest.example</p><p>☏ +1 555 014 2290</p>
</div>
<div class="f-col abs" style="left:851px;top:4112px">
  <h4>Newsletter Signup</h4><p>Subscribe To Our Newsletter</p>
</div>
<div class="news abs"><span>Email</span><b>Subscribe</b></div>
<div class="f-line abs"></div>
<div class="f-copy abs">© 2025 Corbel Crest Lighting - Commercial &amp; Residential Landscape Lighting</div>
<div class="f-legal abs">All rights reserved. | Privacy Policy</div>

</body>
</html>
```